A NEW UPDATED VERSION OF A 4"X9" RACK CARD

A NEW UPDATED VERSION OF A RACK CARD, THIS CARD IS 5 YEARS OLD AND WE WANT SOMETHING NEW AND FRESH AND MORE UPDATED TO TODAY. MARKET TO A YOUNGER CROWD. USE THE ATTACHED RACK CARD FOR THE INFO AND VERBAGE AND LOGO TO BE USED. DO NOT USE THE PICTURE OF THE BUILDIING, don't use the picture of the 2 guys. USED THE ATTACHED POST CARDS AS COLORS AND REFERENCE.

Target Market(s)

25-45

Industry/Entity Type

HOME INSPECTIONS

```html
<!DOCTYPE html>
<html lang="en">
<head>
<meta charset="utf-8">
<title>Multi-Inspector Firm – Vantrel Home Inspections</title>
<link href="https://fonts.googleapis.com/css2?family=Anton&family=Montserrat:wght@800;900&display=swap" rel="stylesheet">
<style>
  :root {
    --gold: #eeb838;
    --blue: #0b4f9c;
    --blue-deep: #08407f;
    --ink: #0d4f9c;
    --black: #121418;
    --white: #ffffff;
    --green: #0a6333;
    --coral: #e87b72;
    --orange: #ef8a2a;
    --slate: #4f5480;
    --teal: #45bcd0;
    --amber: #f0921f;
    --plum: #9c528b;
    --yellow: #f5c200;
  }
  * { margin: 0; padding: 0; box-sizing: border-box; }
  html, body { width: 1200px; height: 2700px; overflow: hidden; }
  body { position: relative; background: var(--blue); font-family: "Montserrat", sans-serif; }

  .header-band {
    position: absolute; left: 0; top: 0; width: 1200px; height: 201px;
    background: var(--gold);
    display: flex; align-items: center; justify-content: center;
  }
  .headline {
    font-family: "Anton", sans-serif; font-size: 118px; line-height: 1;
    color: var(--ink); letter-spacing: -1px; transform: scaleX(0.92);
    text-shadow: 3px 4px 4px rgba(0,0,0,0.45);
  }

  .services-field {
    position: absolute; left: 0; top: 201px; width: 1200px; height: 2073px;
    background: linear-gradient(135deg, #0d56a6 0%, var(--blue) 45%, var(--blue-deep) 100%);
  }
  .service-map { position: absolute; left: 0; top: 0; }
  .node-label {
    font-family: "Montserrat", sans-serif; font-weight: 900; font-size: 19px;
    fill: var(--white); text-anchor: middle; letter-spacing: 0.5px;
  }
  .node-label.dark { fill: var(--black); }

  .extras-frame {
    position: absolute; left: 58px; top: 1719px; width: 1087px; height: 524px;
    border: 4px solid var(--white); border-radius: 64px;
  }
  .extra-card {
    position: absolute; width: 408px; height: 190px; background: var(--white);
    border-radius: 62px; display: flex; align-items: center;
  }
  .extra-card .icon { width: 96px; height: 110px; margin-left: 46px; flex: none; display: flex; align-items: center; justify-content: center; }
  .extra-card .icon-slot { width: 80px; height: 100px; border-radius: 18px; background: #d7e3f3; }
  .extra-card .label {
    flex: 1; text-align: center; font-family: "Anton", sans-serif; font-size: 40px;
    line-height: 1.12; color: var(--ink); padding-right: 30px; text-transform: uppercase;
    transform: scaleX(0.9);
  }
  .card-mold { left: 144px; top: 1764px; }
  .card-radon { left: 649px; top: 1764px; }
  .card-termite { left: 144px; top: 2009px; }
  .card-water { left: 649px; top: 2009px; }

  .footer-band {
    position: absolute; left: 0; top: 2274px; width: 1200px; height: 346px;
    background: var(--gold);
  }
  .brand-mark {
    position: absolute; left: 0; top: 40px; width: 1200px;
    display: flex; align-items: center; justify-content: center; gap: 20px;
  }
  .brand-dot { width: 110px; height: 110px; border-radius: 50%; background: var(--ink); }
  .brand-mark-name { font-family: "Anton", sans-serif; font-size: 40px; color: var(--ink); line-height: 1.1; }
  .brand-name {
    position: absolute; left: 0; top: 190px; width: 1200px; text-align: center;
    font-family: "Anton", sans-serif; font-size: 86px; line-height: 1; color: var(--ink);
    transform: scaleX(0.88); text-shadow: 3px 4px 4px rgba(0,0,0,0.4);
  }
  .web-bar {
    position: absolute; left: 0; top: 2620px; width: 1200px; height: 80px;
    background: var(--black); display: flex; align-items: center; justify-content: center;
  }
  .web-address { font-family: "Montserrat", sans-serif; font-weight: 800; font-size: 40px; color: var(--white); letter-spacing: 0.5px; }
</style>
</head>
<body>
  <header class="header-band">
    <h1 class="headline">MULTI-INSPECTOR FIRM</h1>
  </header>

  <section class="services-field">
    <svg class="service-map" width="1200" height="2073" viewBox="0 201 1200 2073" aria-label="Our services diagram">
      <defs>
        <filter id="node-shadow" x="-30%" y="-30%" width="160%" height="160%">
          <feDropShadow dx="6" dy="8" stdDeviation="8" flood-color="#000" flood-opacity="0.35"/>
        </filter>
      </defs>
      <g fill="none" stroke-linecap="round">
        <line x1="596" y1="515" x2="596" y2="866" stroke="#b9d99a" stroke-width="4"/>
        <line x1="596" y1="650" x2="596" y2="866" stroke="#ef8a2a" stroke-width="4"/>
        <line x1="382" y1="624" x2="596" y2="624" stroke="#b9d99a" stroke-width="4"/>
        <line x1="596" y1="624" x2="787" y2="624" stroke="#ef7a3a" stroke-width="4"/>
        <line x1="330" y1="678" x2="520" y2="880" stroke="#b5456a" stroke-width="4"/>
        <line x1="865" y1="680" x2="668" y2="888" stroke="#f5b800" stroke-width="4"/>
        <line x1="602" y1="1062" x2="602" y2="1445" stroke="#c0392b" stroke-width="4"/>
        <line x1="602" y1="1062" x2="602" y2="1280" stroke="#7d4c8c" stroke-width="4"/>
        <line x1="389" y1="1323" x2="793" y2="1323" stroke="#e8512f" stroke-width="4"/>
        <line x1="520" y1="1055" x2="335" y2="1245" stroke="#4b4c86" stroke-width="4"/>
        <line x1="668" y1="1040" x2="760" y2="1136" stroke="#f5c200" stroke-width="12"/>
        <line x1="760" y1="1136" x2="860" y2="1245" stroke="#f5c200" stroke-width="4"/>
      </g>
      <path d="M596 580 Q603 617 640 624 Q603 631 596 668 Q589 631 552 624 Q589 617 596 580Z" fill="#fff"/>
      <path d="M602 1279 Q609 1316 646 1323 Q609 1330 602 1367 Q595 1330 558 1323 Q595 1316 602 1279Z" fill="#fff"/>
      <g filter="url(#node-shadow)">
        <circle cx="432" cy="781" r="30" fill="#e8674f"/>
        <circle cx="596" cy="752" r="30" fill="#ef8a2a"/>
        <circle cx="762" cy="781" r="30" fill="#ef8a2a"/>
        <circle cx="433" cy="1136" r="30" fill="#463f7a"/>
        <circle cx="602" cy="1187" r="30" fill="#8f2f6a"/>
        <circle cx="760" cy="1136" r="30" fill="#f5c200"/>
      </g>
      <g fill="none" stroke="#fff" stroke-width="4" stroke-linecap="round">
        <path d="M414 790 A20 20 0 0 1 428 766"/>
        <path d="M578 761 A20 20 0 0 1 592 737"/>
        <path d="M744 790 A20 20 0 0 1 758 766"/>
        <path d="M415 1145 A20 20 0 0 1 429 1121"/>
        <path d="M742 1145 A20 20 0 0 1 756 1121"/>
      </g>
      <g fill="none" stroke-width="4">
        <path d="M530 478 A112 112 0 0 1 680 290" stroke="#0a6333"/>
        <path d="M150 560 A100 100 0 0 0 190 726" stroke="#e87b72"/>
        <path d="M1020 535 A110 110 0 0 1 1020 724" stroke="#f5b800"/>
        <path d="M548 870 A108 108 0 0 0 552 1066" stroke="#8f2f6a"/>
        <path d="M148 1250 A100 100 0 0 0 200 1392" stroke="#2a7b7d"/>
        <path d="M1000 1187 A108 108 0 0 1 1000 1394" stroke="#f5b800"/>
        <path d="M500 1600 A112 112 0 0 1 690 1520" stroke="#8f2f6a"/>
      </g>
      <g filter="url(#node-shadow)">
        <circle cx="596" cy="385" r="100" fill="var(--green)"/>
        <circle cx="235" cy="629" r="100" fill="var(--coral)"/>
        <circle cx="964" cy="629" r="100" fill="var(--orange)"/>
        <circle cx="600" cy="964" r="100" fill="var(--slate)"/>
        <circle cx="235" cy="1291" r="100" fill="var(--teal)"/>
        <circle cx="961" cy="1291" r="100" fill="var(--amber)"/>
        <circle cx="600" cy="1553" r="100" fill="var(--plum)"/>
      </g>
      <g fill="none" stroke="#fff" stroke-width="5" stroke-linecap="round">
        <path d="M630 298 A80 80 0 0 1 665 335"/>
        <path d="M158 593 A85 85 0 0 1 213 547"/>
        <path d="M887 593 A85 85 0 0 1 942 547"/>
        <path d="M515 940 A85 85 0 0 1 560 890"/>
        <path d="M158 1255 A85 85 0 0 1 213 1209"/>
        <path d="M884 1255 A85 85 0 0 1 939 1209"/>
        <path d="M625 1468 A80 80 0 0 1 680 1515"/>
      </g>
      <text class="node-label" x="596" y="379">PRE-LISTING</text>
      <text class="node-label" x="596" y="402">INSPECTIONS</text>
      <text class="node-label" x="235" y="623">COMMERCIAL</text>
      <text class="node-label" x="235" y="646">INSPECTIONS</text>
      <text class="node-label" x="964" y="623">HOME</text>
      <text class="node-label" x="964" y="646">INSPECTIONS</text>
      <text class="node-label" x="600" y="958">OUR</text>
      <text class="node-label" x="600" y="981">SERVICES</text>
      <text class="node-label" x="235" y="1285">4-POINT</text>
      <text class="node-label" x="235" y="1308">INSPECTIONS</text>
      <text class="node-label" x="961" y="1285">WIND</text>
      <text class="node-label" x="961" y="1308">MITIGATIONS</text>
      <text class="node-label dark" x="600" y="1536">BUILDER’S</text>
      <text class="node-label dark" x="600" y="1559">WARRANTY</text>
      <text class="node-label dark" x="600" y="1582">INSPECTIONS</text>
    </svg>
  </section>

  <div class="extras-frame"></div>

  <div class="extra-card card-mold">
    <div class="icon">
      <svg width="92" height="92" viewBox="0 0 92 92" fill="none" stroke="#0d4f9c" stroke-width="3">
        <circle cx="46" cy="46" r="42"/><circle cx="46" cy="46" r="35"/>
        <circle cx="34" cy="36" r="6"/><circle cx="56" cy="30" r="4"/><circle cx="58" cy="56" r="7"/>
        <circle cx="36" cy="60" r="4"/><circle cx="46" cy="46" r="3"/>
      </svg>
    </div>
    <div class="label">Mold<br>Testing</div>
  </div>

  <div class="extra-card card-radon">
    <div class="icon"><div class="icon-slot" role="img" aria-label="Gas mask icon"></div></div>
    <div class="label">Radon<br>Testing</div>
  </div>

  <div class="extra-card card-termite">
    <div class="icon"><div class="icon-slot" role="img" aria-label="Termite icon"></div></div>
    <div class="label">WDO/Termite<br>Inspections</div>
  </div>

  <div class="extra-card card-water">
    <div class="icon">
      <svg width="100" height="116" viewBox="0 0 100 116" fill="none" stroke="#0d4f9c" stroke-width="4" stroke-linecap="round">
        <path d="M6 8 H94 L86 108 H14 Z" stroke-linejoin="round"/>
        <path d="M10 22 H90"/>
        <path d="M12 46 q10 -8 19 0 t19 0 t19 0 t19 0"/>
        <path d="M13 64 q10 -8 19 0 t19 0 t19 0 t18 0"/>
        <path d="M14 82 q10 -8 18 0 t18 0 t18 0 t18 0"/>
      </svg>
    </div>
    <div class="label">Water<br>Quality<br>Testing</div>
  </div>

  <footer class="footer-band">
    <div class="brand-mark">
      <div class="brand-dot"></div>
      <div class="brand-mark-name">VANTREL<br>HOME INSPECTIONS</div>
    </div>
    <div class="brand-name">VANTREL HOME INSPECTIONS</div>
  </footer>

  <div class="web-bar">
    <span class="web-address">www.VantrelHomeInspections.com</span>
  </div>
</body>
</html>
```